College Advising Business Card Design

We need a business card design for a new company. We advise students and their families on finding the right colleges to apply to; the application process; creating resumes; writing essays; and once students are accepted, figuring out what the best fit is. We pride ourselves on highly personal service, and we travel the country to learn about schools. The visual we have used on our website is a picture of a graduation caps tossed into the blue sky. See my website.

Target Market(s)

Parents of high school students

Industry/Entity Type

Travel

Contact Information for Business Card

COLLEGE IS THE DREAM. LET US HELP YOU FIND THE DESTINATION.

Corinne Halvast Perrow and Associates
College Admissions Advising and Essay Guidance
quill@corinnehalvastperrow.example
555-417-BEST (2378)
Follow us on Facebook

```html
<!DOCTYPE html>
<html lang="en">
<head>
<meta charset="utf-8">
<title>Corinne Halvast – College Admissions Advising Card</title>
<link rel="stylesheet" href="https://fonts.googleapis.com/css2?family=Saira+Semi+Condensed:wght@600;700&family=Tinos&display=swap">
<style>
  :root {
    --sky-deep: #0a4a95;
    --sky-mid: #3f87cf;
    --sky-light: #b7d6ee;
    --horizon: #e8f1f6;
    --grass-light: #6f9b3c;
    --grass-dark: #1f4714;
    --ink-white: #ffffff;
    --band: rgba(22, 66, 118, 0.62);
  }
  html, body {
    margin: 0;
    padding: 0;
    overflow: hidden;
    background: #ffffff;
  }
  .card {
    position: relative;
    width: 1200px;
    height: 702px;
    overflow: hidden;
    color: var(--ink-white);
  }
  .card__backdrop {
    position: absolute;
    inset: 0;
    background:
      linear-gradient(180deg, transparent 0%, transparent 72%, var(--grass-light) 80%, var(--grass-dark) 100%),
      radial-gradient(ellipse at 95% 78%, var(--horizon) 0%, transparent 35%),
      linear-gradient(180deg, var(--sky-deep) 0%, var(--sky-mid) 38%, var(--sky-light) 70%, var(--horizon) 78%);
  }
  .tagline {
    position: absolute;
    top: 30px;
    left: 0;
    width: 100%;
    margin: 0;
    text-align: center;
    font-family: "Saira Semi Condensed", sans-serif;
    font-weight: 700;
    font-size: 25px;
    letter-spacing: 8px;
    text-shadow: 0 1px 3px rgba(0,0,0,0.35);
  }
  .identity {
    position: absolute;
    top: 258px;
    left: 0;
    width: 100%;
    text-align: center;
    font-family: "Saira Semi Condensed", sans-serif;
    font-weight: 700;
    text-shadow: 0 1px 4px rgba(0,0,0,0.45);
  }
  .identity__name {
    margin: 0;
    font-size: 42px;
    letter-spacing: 9px;
    line-height: 1.1;
  }
  .identity__role {
    margin: 4px 0 0;
    font-size: 23px;
    letter-spacing: 5px;
  }
  .contact {
    position: absolute;
    left: 0;
    top: 566px;
    width: 100%;
    font-family: "Tinos", serif;
    font-size: 17px;
    letter-spacing: 5.2px;
  }
  .contact__row {
    display: flex;
    justify-content: center;
    gap: 14px;
    height: 36px;
    align-items: center;
  }
  .contact__item {
    display: inline-flex;
    align-items: center;
    gap: 6px;
    background: var(--band);
    padding: 2px 10px;
    white-space: nowrap;
  }
  .contact__icon {
    width: 18px;
    height: 18px;
    flex: none;
    fill: var(--ink-white);
  }
  .contact__square {
    width: 15px;
    height: 15px;
    background: var(--ink-white);
    flex: none;
  }
</style>
</head>
<body>
<div class="card">
  <div class="card__backdrop" role="img" aria-label="Photograph of graduates in gowns silhouetted against a blue sky, tossing their caps above a grassy field"></div>

  <p class="tagline">COLLEGE IS THE DREAM. LET US HELP YOU FIND THE DESTINATION</p>

  <div class="identity">
    <h1 class="identity__name">Corinne Halvast</h1>
    <p class="identity__role">College Admissions Advising &amp; Essay Guidance</p>
  </div>

  <div class="contact">
    <div class="contact__row">
      <span class="contact__item">
        <svg class="contact__icon" viewBox="0 0 24 24"><path d="M6.6 10.8a15.1 15.1 0 0 0 6.6 6.6l2.2-2.2c.3-.3.7-.4 1-.2 1.1.4 2.3.6 3.6.6.6 0 1 .4 1 1V20c0 .6-.4 1-1 1C10.6 21 3 13.4 3 4c0-.6.4-1 1-1h3.5c.6 0 1 .4 1 1 0 1.3.2 2.5.6 3.6.1.3 0 .7-.2 1z"/></svg>
        1-555-417-BEST (2378)
      </span>
      <span class="contact__item">
        <svg class="contact__icon" viewBox="0 0 24 24"><path d="M7 1h10a2 2 0 0 1 2 2v18a2 2 0 0 1-2 2H7a2 2 0 0 1-2-2V3a2 2 0 0 1 2-2zm0 3v14h10V4zm5 15.5a1 1 0 1 0 0 2 1 1 0 0 0 0-2z"/></svg>
        1-555-417-2378
      </span>
    </div>
    <div class="contact__row">
      <span class="contact__item">
        <svg class="contact__icon" viewBox="0 0 24 24"><path d="M12 2a7 7 0 0 0-7 7c0 5.2 7 13 7 13s7-7.8 7-13a7 7 0 0 0-7-7zm0 9.5a2.5 2.5 0 1 1 0-5 2.5 2.5 0 0 1 0 5z"/></svg>
        18 Quarry Bend Road West, Alder Falls, New Jersey 07999
      </span>
    </div>
    <div class="contact__row">
      <span class="contact__item">
        <svg class="contact__icon" viewBox="0 0 24 24"><path d="M2 5h20v14H2zm2 2v.5l8 5.5 8-5.5V7zm0 3v7h16v-7l-8 5.5z"/></svg>
        quill@corinnehalvastperrow.example
      </span>
      <span class="contact__item">
        <svg class="contact__icon" viewBox="0 0 24 24"><path d="M12 2a10 10 0 1 0 0 20 10 10 0 0 0 0-20zm6.9 6h-2.9a15.7 15.7 0 0 0-1.4-3.6A8 8 0 0 1 18.9 8zM12 4c.8 1.2 1.5 2.5 1.9 4h-3.8c.4-1.5 1.1-2.8 1.9-4zM4.3 14a8 8 0 0 1 0-4h3.4a16 16 0 0 0 0 4zm.8 2h2.9c.3 1.3.8 2.5 1.4 3.6A8 8 0 0 1 5.1 16zM8 8H5.1a8 8 0 0 1 4.3-3.6C8.8 5.5 8.3 6.7 8 8zm4 12c-.8-1.2-1.5-2.5-1.9-4h3.8c-.4 1.5-1.1 2.8-1.9 4zm2.3-6H9.7a14.7 14.7 0 0 1 0-4h4.6a14.7 14.7 0 0 1 0 4zm.3 5.6c.6-1.1 1.1-2.3 1.4-3.6h2.9a8 8 0 0 1-4.3 3.6zm1.7-5.6a16 16 0 0 0 0-4h3.4a8 8 0 0 1 0 4z"/></svg>
        www.corinnehalvastperrow.example
      </span>
    </div>
    <div class="contact__row">
      <span class="contact__item">
        <span class="contact__square"></span>
        corinnehalvastperrow
      </span>
      <span class="contact__item">
        <span class="contact__square"></span>
        corinnehalvastperrow
      </span>
    </div>
  </div>
</div>
</body>
</html>
```